Home Design company focused on remodel and enhancement of kitchens and bathroorms

I already have a logo designed by ArtHive, I now need a design for my business cards.
The company is in the remodeling and enhancement industry for homes, focusing on kitchens and bathrooms, however, we can remodel or enhance every room in a home, an office space, etc.

The company's name is VORNETT HOME DESIGN, LLC

We'll focus on clients in the Rio Grande Valley, Texas. Primarily McAllen, Edinburg, Pharr, Mission, Brownsville and South Padre Island.

The design on the business card should transmit reliability, professionalism anda bit of upscale design.

The logo is in black and white, and would like to keep it that way.

The information that needs to be printed in the business cards is:
Company's name: Vornett Home Design
My name: Mira Lindqvist
Address, phone and email:
2715 N Parkline Rd, Ste 318
Larkmont, NV 70913
(555) 731 2958
mlindqvist@vornettstudio.com
Website: vornettstudio.com

```html
<!DOCTYPE html>
<html lang="en">
<head>
<meta charset="utf-8">
<title>Vornett Home Design – Business Card</title>
<link rel="stylesheet" href="https://fonts.googleapis.com/css2?family=Arimo:wght@400&family=Montserrat:wght@400&display=swap">
<style>
  :root {
    --backdrop: #d2d3d5;
    --paper: #fafafa;
    --ink: #0a0a0a;
    --rule: #9c9c9c;
    --reverse: #ffffff;
    --shadow: rgba(0, 0, 0, 0.28);
  }
  * { margin: 0; padding: 0; box-sizing: border-box; }
  html, body {
    width: 1199px;
    height: 1200px;
    overflow: hidden;
    background: var(--backdrop);
    font-family: "Arimo", Arial, sans-serif;
    color: var(--ink);
  }
  .card {
    position: absolute;
    left: 286px;
    width: 587px;
    height: 352px;
    box-shadow: 14px 12px 22px var(--shadow);
  }
  .card--front { top: 184px; background: var(--paper); }
  .card--back { top: 649px; background: var(--ink); color: var(--reverse); }

  .front__band {
    position: absolute;
    left: 0; bottom: 0;
    width: 100%;
    height: 43px;
    background: var(--ink);
  }
  .front__divider {
    position: absolute;
    left: 293px;
    top: 35px;
    width: 1.5px;
    height: 257px;
    background: var(--rule);
  }

  .wordmark {
    position: absolute;
    display: flex;
    align-items: center;
    gap: 10px;
    font-family: "Montserrat", Arial, sans-serif;
    font-weight: 400;
    text-transform: uppercase;
  }
  .wordmark__square {
    width: 30px;
    height: 30px;
    border: 2.5px solid currentColor;
  }
  .wordmark__name {
    font-size: 12.5px;
    line-height: 13px;
    letter-spacing: 3px;
  }
  .card--front .wordmark { left: 70px; top: 158px; }
  .card--back .wordmark { left: 50%; top: 156px; transform: translateX(-50%); }

  .holder {
    position: absolute;
    left: 331px;
    top: 88px;
    font-size: 21px;
    font-weight: 400;
    letter-spacing: 0.5px;
    text-transform: uppercase;
  }
  .contact {
    position: absolute;
    left: 323px;
    top: 154px;
    list-style: none;
    font-size: 14px;
  }
  .contact li {
    display: flex;
    align-items: center;
    margin-bottom: 10px;
  }
  .contact svg {
    flex: none;
    width: 20px;
    height: 16px;
    margin-right: 15px;
  }
  .contact li.contact__address {
    align-items: flex-start;
    line-height: 23px;
    margin-bottom: 8px;
  }
  .contact__address svg { margin-top: 6px; }
  .contact__phone { font-size: 15px; }

  .back__site {
    position: absolute;
    left: 0;
    width: 100%;
    top: 296px;
    text-align: center;
    font-size: 14px;
    letter-spacing: 2.2px;
  }
</style>
</head>
<body>

<section class="card card--front" aria-label="Business card front">
  <div class="wordmark">
    <span class="wordmark__square"></span>
    <span class="wordmark__name">Vornett<br>Home<br>Design</span>
  </div>

  <div class="front__divider"></div>

  <h1 class="holder">Mira Lindqvist</h1>

  <ul class="contact">
    <li class="contact__address">
      <svg viewBox="0 0 20 16" aria-hidden="true"><path fill="#0a0a0a" d="M10 0a5 5 0 0 0-5 5c0 3.8 5 11 5 11s5-7.2 5-11a5 5 0 0 0-5-5zm0 7a2 2 0 1 1 0-4 2 2 0 0 1 0 4z"/></svg>
      <span>2715 N Parkline Rd, Ste 318<br>Larkmont, NV 70913</span>
    </li>
    <li class="contact__phone">
      <svg viewBox="0 0 20 16" aria-hidden="true"><path fill="#0a0a0a" d="M4 1l3 0 1.5 3.5-2 1.5c1 2 3 4 5 5l1.5-2 3.5 1.5v3c0 1-1 1.5-2 1.5C8 15 2 9 2 3c0-1 1-2 2-2z"/></svg>
      <span>(555) 731 2958</span>
    </li>
    <li>
      <svg viewBox="0 0 20 16" aria-hidden="true"><rect x="3" y="3" width="14" height="10" fill="#0a0a0a"/><path d="M3 3.5l7 5.5 7-5.5" fill="none" stroke="#fafafa" stroke-width="1.2"/></svg>
      <span>mlindqvist@vornettstudio.com</span>
    </li>
    <li>
      <svg viewBox="0 0 20 16" aria-hidden="true"><g fill="none" stroke="#0a0a0a" stroke-width="1.2"><circle cx="10" cy="8" r="6"/><ellipse cx="10" cy="8" rx="2.6" ry="6"/><path d="M4 8h12M5 5h10M5 11h10"/></g></svg>
      <span>www.vornettstudio.com</span>
    </li>
  </ul>

  <div class="front__band"></div>
</section>

<section class="card card--back" aria-label="Business card back">
  <div class="wordmark">
    <span class="wordmark__square"></span>
    <span class="wordmark__name">Vornett<br>Home<br>Design</span>
  </div>
  <p class="back__site">www.vornettstudio.com</p>
</section>

</body>
</html>
```